One Page Magazine Ad for New Apartment in Calgary, AB Canada

We need a one page magazine ad for a new apartment community in Calgary, Alberta.

We pride ourselves in providing the highest level of customer service and the best amenities for our community.

COMMUNITY HIGHLIGHTS

- Brand new luxury apartment rental community in the exciting Calgary Beltline neighborhood
- 13 unique spacious floor plans fit for every lifestyle (1BR-1BATH, 2BR-1BATH & 2BR-2BATH)
- Professionally managed
- On-site staff during business hours to help you with any of your needs
- Pet-friendly community
- State of the art Fitness Facility
- 2 rooftop terraces outfitted with 8 Community Brimfield BBQs
- Great area for entertaining guests and a safe spot to take your dog out for some fresh air without leaving the building
- 2 resident lounges with multimedia suite, 60-inch TVs, Vexa Two, Silver Pin Arcade system, Poker table
- Great venues to host your next party, open 24/7 free to use and bookable by residents for free!
- Monthly resident events and parties hosted by the on-site staff
- Underground secured guest and resident parking available
- Electric Car Charging Stations
- Garbage & Recycling chutes on every floor
- Controlled Access/Building
- Gated Underground Parking Garage
- Adjacent to the Beltline neighborhood bike lane on 27th Avenue SW
- Elevators - Underground Secured Bike Storage and bike repair workstation
- On-site Maintenance
- Crate Keeper Package Management System
- Additional Storage Available
- Footsteps away from the local Fairmart Grocery and Fairmart Wine Store
- Minutes away from the new free leash dog park Wexley Park

APARTMENT AMENITIES

- Gourmet Kitchen with 4 piece Stainless Steel Appliances (Stove, Fridge, Microwave and Dishwasher)
- In suite dryer and washer
- Large Closets
- Patio/Balcony
- City and mountain views
- Ceramic Tile and Laminate Hardwood Flooring
- Quartz Counter-tops
- Roller Blinds for all Windows
- Walk-in Closets

For branding style, floor plans, amenities and photos please visit our website www.stayatthevorn.com

Target Market(s)

Young Adults and Recently Single Market

Industry/Entity Type

Real Estate

Font styles to use
Sans Serif

Colors
f37122

Requirements
Must have
• - Pictures of the community
• - Possibly use of a stock photo

```html
<!DOCTYPE html>
<html lang="en">
<head>
<meta charset="utf-8">
<title>The Vorn – Magazine Ad</title>
<link rel="stylesheet" href="https://fonts.googleapis.com/css2?family=Montserrat:wght@300;400;500;700&display=swap">
<style>
  :root {
    --orange: #f37122;
    --stage: #5e5e5e;
    --paper: #ffffff;
    --band: #d4d4d6;
    --ink: #1a1a1a;
    --ink-soft: #333333;
    --logo-grey: #5a5a5a;
    --rule-grey: #c9c9cb;
    --sky: #8aa7c9;
    --photo-deep: #3a3f47;
  }
  * { box-sizing: border-box; margin: 0; padding: 0; }
  html, body { width: 1200px; height: 640px; overflow: hidden; }
  body {
    background: var(--stage);
    font-family: "Montserrat", Arial, sans-serif;
    position: relative;
  }
  .ad-page {
    position: absolute;
    left: 380px; top: 12px;
    width: 440px; height: 616px;
    background: var(--paper);
    box-shadow: 0 3px 10px rgba(0,0,0,.35);
    overflow: hidden;
  }
  .brand {
    position: absolute;
    left: 0; top: 72px; width: 263px;
    text-align: center;
    font-weight: 300;
    font-size: 22px;
    letter-spacing: 6px;
    color: var(--logo-grey);
  }
  .hero-photo {
    position: absolute;
    left: 0; top: 141px; width: 252px; height: 183px;
    background: linear-gradient(180deg, var(--sky) 0%, #b9c6d4 45%, #6d6a68 70%, var(--photo-deep) 100%);
  }
  .gallery {
    position: absolute;
    left: 0; top: 336px; width: 252px;
    display: grid;
    grid-template-columns: repeat(3, 82px);
    column-gap: 3px;
    row-gap: 7px;
  }
  .gallery-photo {
    height: 53px;
    border-bottom: 2px solid var(--orange);
  }
  .tone-a { background: linear-gradient(160deg, #2c2f36, #55585f); }
  .tone-b { background: linear-gradient(160deg, #3a3d44, #6b6258); }
  .tone-c { background: linear-gradient(160deg, #4b5566, #8a7d6c); }
  .tone-d { background: linear-gradient(160deg, #e6e6e4, #a9a39a); }
  .tone-e { background: linear-gradient(160deg, #d9dcdc, #3fa6a8); }
  .tone-f { background: linear-gradient(160deg, #2a2b30, #7a4a3a); }
  .tone-g { background: linear-gradient(160deg, #cfd2d3, #6f6458); }
  .tone-h { background: linear-gradient(160deg, #9aa3ac, #3b3b3b); }
  .tone-i { background: linear-gradient(160deg, #d8cfc4, #3f8f88); }

  .highlights {
    position: absolute;
    left: 263px; top: 0; width: 177px; height: 518px;
    background: var(--orange);
    color: #fff;
    padding: 22px 10px 0 15px;
  }
  .highlights-title {
    font-weight: 700;
    font-size: 15.5px;
    line-height: 18px;
  }
  .highlights-rule {
    position: absolute;
    right: 0; top: 41px; width: 38px; height: 5px;
    background: var(--rule-grey);
  }
  .highlights-list {
    list-style: none;
    margin-top: 13px;
    font-size: 7.1px;
    line-height: 8.3px;
  }
  .highlights-list li {
    position: relative;
    padding-left: 10px;
    margin-bottom: 3.1px;
  }
  .highlights-list li::before,
  .amenities-list li::before {
    content: "-";
    position: absolute;
    left: 0;
  }

  .amenities {
    position: absolute;
    left: 0; top: 518px; width: 440px; height: 98px;
    background: var(--band);
  }
  .amenities-title {
    position: absolute;
    left: 27px; top: 19px;
    font-weight: 700;
    font-size: 15.5px;
    line-height: 19px;
    color: var(--ink);
  }
  .amenities-rule {
    position: absolute;
    left: 27px; top: 64px; width: 49px; height: 5px;
    background: var(--orange);
  }
  .amenities-list {
    position: absolute;
    top: 22px;
    list-style: none;
    font-size: 6.9px;
    line-height: 8.4px;
    color: var(--ink-soft);
  }
  .amenities-list li { position: relative; padding-left: 8px; }
  .amenities-list.col-one { left: 150px; width: 140px; }
  .amenities-list.col-two { left: 300px; width: 130px; }
</style>
</head>
<body>
  <main class="ad-page">
    <div class="brand">THE VORN</div>

    <div class="hero-photo" role="img" aria-label="Street-level photo of the apartment tower under a blue cloudy sky"></div>

    <div class="gallery">
      <div class="gallery-photo tone-a" role="img" aria-label="Resident lounge with dark walls"></div>
      <div class="gallery-photo tone-b" role="img" aria-label="Games room with pool table"></div>
      <div class="gallery-photo tone-c" role="img" aria-label="Poker table in the lounge"></div>
      <div class="gallery-photo tone-d" role="img" aria-label="Bright open kitchen"></div>
      <div class="gallery-photo tone-e" role="img" aria-label="Living room with teal sofa"></div>
      <div class="gallery-photo tone-f" role="img" aria-label="Fitness facility"></div>
      <div class="gallery-photo tone-g" role="img" aria-label="Bedroom with large window"></div>
      <div class="gallery-photo tone-h" role="img" aria-label="Rooftop terrace with giant chess set"></div>
      <div class="gallery-photo tone-i" role="img" aria-label="Lounge with arcade and seating"></div>
    </div>

    <section class="highlights">
      <h2 class="highlights-title">Community<br>Highlights</h2>
      <span class="highlights-rule"></span>
      <ul class="highlights-list">
        <li>Brand new luxury apartment rental community in the exciting Calgary Beltline neighborhood</li>
        <li>13 unique spacious floor plans fit for every lifestyle (1BR-1BATH, 2BR-1BATH &amp; 2BR-2BATH)</li>
        <li>Professionally managed</li>
        <li>On-site staff during business hours to help you with any of your needs</li>
        <li>Pet-friendly community</li>
        <li>State of the art Fitness Facility</li>
        <li>2 rooftop terraces outfitted with 8 Community Brimfield BBQs</li>
        <li>Great area for entertaining guests and a safe spot to take your dog out for some fresh air without leaving the building</li>
        <li>2 resident lounges with multimedia suite, 60-inch TVs, Vexa Two, Silver Pin Arcade system, Poker table</li>
        <li>Great venues to host your next party, open 24/7 free to use and bookable by residents for free!</li>
        <li>Monthly resident events and parties hosted by the on-site staff</li>
        <li>Underground secured guest and resident parking available</li>
        <li>Electric Car Charging Stations</li>
        <li>Garbage &amp; Recycling chutes on every floor</li>
        <li>Controlled Access/Building</li>
        <li>Gated Underground Parking Garage</li>
        <li>Adjacent to the Beltline neighborhood bike lane on 27th Avenue SW</li>
        <li>Elevators - Underground Secured Bike Storage and bike repair workstation</li>
        <li>On-site Maintenance</li>
        <li>Crate Keeper Package Management System</li>
        <li>Additional Storage Available</li>
        <li>Footsteps away from the local Fairmart Grocery and Fairmart Wine Store</li>
        <li>Minutes away from the new free leash dog park Wexley Park</li>
      </ul>
    </section>

    <section class="amenities">
      <h2 class="amenities-title">Apartment<br>Amenities</h2>
      <span class="amenities-rule"></span>
      <ul class="amenities-list col-one">
        <li>Gourmet Kitchen with 4 piece Stainless Steel Appliances (Stove, Fridge, Microwave and Dishwasher)</li>
        <li>In suite dryer and washer</li>
        <li>Large Closets</li>
        <li>Patio/Balcony</li>
      </ul>
      <ul class="amenities-list col-two">
        <li>City and mountain views</li>
        <li>Ceramic Tile and Laminate Hardwood Flooring</li>
        <li>Quartz Counter-tops</li>
        <li>Roller Blinds for all Windows</li>
        <li>Walk-in Closets</li>
      </ul>
    </section>
  </main>
</body>
</html>
```